Build PowerPoint for New Logo & Letterhead

I have started my own consulting firm and created a logo and letterhead (attached) am looking PowerPoint template. My name is Dorrit Okonkwo-Haverly and the company is called Birchpoint Consulting. We primarily use PowerPoint files to display analyses, maps and key talking points from interviews and/or recommendations. We use the documents more to facilitate discussion with our target audiences. Most of the time our PowerPoint document is printed as handouts for our clients and not projected.

Target Market(s)

Healthcare provider organizations (hospitals, health systems, physician groups)

Industry/Entity Type

Healthcare

Font styles to use
Sans Serif

Colors
abd036
1f9ad1
0355a3

Requirements
Must have
• I would like to cover page to play off of the letterhead in some fashion. I want the design to provide plenty of space for text, graphics, maps, pictures, etc.
• We will usually include our clients logo somewhere on the document. Historically it is prominent on the cover page and then in one of the corners on all of the pages thereafter.

```html
<!DOCTYPE html>
<html lang="en">
<head>
<meta charset="utf-8">
<title>Pie Charts – Birchpoint Consulting</title>
<link rel="stylesheet" href="https://fonts.googleapis.com/css2?family=Roboto+Condensed:wght@400;700&display=swap">
<style>
  :root {
    --green: #abd036;
    --green-light: #9ecb3a;
    --green-dark: #5a8a00;
    --sky: #1f9ad1;
    --sky-bright: #0ab8e8;
    --navy: #0355a3;
    --teal: #1089a8;
    --heading-teal: #1a8fb0;
    --grey-slice: #9a9a9a;
    --page: #f6f6f6;
    --ink: #333333;
    --rule: #c8c8c8;
    --white: #ffffff;
  }
  * { box-sizing: border-box; margin: 0; padding: 0; }
  html, body { width: 1200px; height: 900px; overflow: hidden; }
  body {
    position: relative;
    background: var(--page);
    font-family: "Roboto Condensed", "Arial Narrow", sans-serif;
    color: var(--ink);
  }
  .slide { position: absolute; inset: 0; }
  .header-band { position: absolute; left: 0; top: 0; width: 1200px; height: 78px; background: var(--white); }
  .header-band svg { position: absolute; left: 0; top: 0; }
  .slide-title {
    position: absolute; left: 22px; top: 14px;
    font-size: 42px; font-weight: 700; color: var(--white);
    letter-spacing: 0.5px; line-height: 1;
  }
  .brand-name {
    position: absolute; right: 30px; top: 26px;
    font-size: 22px; font-weight: 700; color: var(--navy); line-height: 1;
  }
  .section-heading {
    position: absolute; left: 36px; top: 146px;
    font-size: 30px; font-weight: 700; color: var(--heading-teal);
    line-height: 1; padding-bottom: 6px;
    border-bottom: 2px solid var(--heading-teal);
  }
  .chart { position: absolute; left: 0; top: 0; }
  .label {
    position: absolute; font-size: 21px; line-height: 32px; color: var(--ink);
    white-space: nowrap;
  }
  .footer { position: absolute; left: 0; bottom: 0; width: 1200px; height: 57px; }
  .footer svg { position: absolute; left: 0; top: 0; }
  .copyright {
    position: absolute; left: 12px; bottom: 8px;
    font-size: 21px; color: var(--white); line-height: 1;
  }
  .page-number {
    position: absolute; right: 15px; bottom: 3px;
    font-size: 20px; font-weight: 700; color: var(--white); line-height: 1;
  }
</style>
</head>
<body>
<main class="slide">
  <header class="header-band">
    <svg width="1200" height="78" viewBox="0 0 1200 78" aria-hidden="true">
      <defs>
        <linearGradient id="headerFill" x1="0" y1="0" x2="1" y2="0">
          <stop offset="0" stop-color="#0a6fb8"/>
          <stop offset="1" stop-color="#0bb0ef"/>
        </linearGradient>
      </defs>
      <polygon points="0,0 1050,0 1002,78 0,78" fill="url(#headerFill)"/>
    </svg>
    <h1 class="slide-title">PROJECT TITLE HERE</h1>
    <div class="brand-name">Birchpoint Consulting</div>
  </header>

  <h2 class="section-heading">PIE CHARTS</h2>

  <svg class="chart" width="1200" height="900" viewBox="0 0 1200 900" role="img" aria-label="Donut chart of communication costs by category">
    <g class="donut" transform="rotate(-90 627 543)" fill="none" stroke-width="97">
      <circle cx="627" cy="543" r="183.5" stroke="var(--green-light)" stroke-dasharray="400.4 1153" stroke-dashoffset="0"/>
      <circle cx="627" cy="543" r="183.5" stroke="var(--grey-slice)" stroke-dasharray="118.5 1153" stroke-dashoffset="-400.4"/>
      <circle cx="627" cy="543" r="183.5" stroke="var(--teal)" stroke-dasharray="64.1 1153" stroke-dashoffset="-518.9"/>
      <circle cx="627" cy="543" r="183.5" stroke="var(--navy)" stroke-dasharray="477.2 1153" stroke-dashoffset="-583"/>
      <circle cx="627" cy="543" r="183.5" stroke="var(--sky-bright)" stroke-dasharray="54.4 1153" stroke-dashoffset="-1060.2"/>
      <circle cx="627" cy="543" r="183.5" stroke="var(--green-dark)" stroke-dasharray="38.4 1153" stroke-dashoffset="-1114.6"/>
    </g>
    <g class="leaders" fill="none" stroke="var(--rule)" stroke-width="1.5">
      <polyline points="854,501 954,501"/>
      <polyline points="768,724 891,724"/>
      <polyline points="656,768 656,815 789,815"/>
      <polyline points="390,545 225,545"/>
      <polyline points="528,324 387,324"/>
      <polyline points="599,308 599,252"/>
    </g>
    <g class="markers" fill="var(--navy)" stroke="var(--white)" stroke-width="3.5">
      <circle cx="854" cy="501" r="12"/>
      <circle cx="768" cy="724" r="12"/>
      <circle cx="656" cy="768" r="12"/>
      <circle cx="390" cy="545" r="12"/>
      <circle cx="528" cy="324" r="12"/>
      <circle cx="599" cy="308" r="12"/>
    </g>
  </svg>

  <p class="label" style="left:966px; top:484px;">Communications<br>Voix Nationales</p>
  <p class="label" style="left:903px; top:710px;">Communications auters</p>
  <p class="label" style="left:798px; top:799px;">Communications auters</p>
  <p class="label" style="left:63px; top:509px;">Communications Data<br>depuis l'etranger</p>
  <p class="label" style="left:206px; top:293px;">Communications<br>Sms/MMS Surtext</p>
  <p class="label" style="left:482px; top:212px;">Communications Sms/MMS</p>

  <footer class="footer">
    <svg width="1200" height="57" viewBox="0 0 1200 57" aria-hidden="true">
      <rect x="0" y="30" width="1200" height="27" fill="var(--green-light)"/>
      <polygon points="0,0 248,0 270,30 270,57 0,57" fill="#8fc031"/>
    </svg>
    <p class="copyright">Copyright text here</p>
    <p class="page-number">01</p>
  </footer>
</main>
</body>
</html>
```